Fernhollow Landscaping Folder Design

I need a graphic designer to design a folder so we can insert informational sheets inside it for customers. The folder must include the company logo, project images, on front and back of folder and slogan " The Experience You Want, The Service You Expect, And The Value You Deserve'

Folder to also include phone numbers : 416 555 0187 as well as the website: www.fernhollowlandscaping.example as well as we gurantee a 24 month warranty.

I have attached sample of size we need.

Pixel Bazaar has also done something similar for me for Tillwood Landscapes

geared toward home owners & commercial/industrial

Landscaping

• open to new trendy font

• Telephone Number, email address, slogan, images,
• images of completed projects incorporated into the front and back of folder as well as the logo
• n/a

```html
<!DOCTYPE html>
<html lang="en">
<head>
<meta charset="utf-8">
<title>Fernhollow Landscaping Folder</title>
<link href="https://fonts.googleapis.com/css2?family=Roboto:wght@300;400;500&display=swap" rel="stylesheet">
<style>
  :root {
    --coral: #d65a5c;
    --coral-dark: #c94c4f;
    --charcoal: #55585a;
    --slate: #8d9093;
    --mist: #e4e4e4;
    --silver: #cfd0d1;
    --mint: #a9dfa6;
    --paper: #ffffff;
    --backdrop: #ece9e4;
    --ink: #3f4244;
  }
  * { margin: 0; padding: 0; box-sizing: border-box; }
  html, body { width: 1200px; height: 750px; overflow: hidden; }
  body {
    background: var(--backdrop);
    font-family: "Roboto", Arial, sans-serif;
    position: relative;
  }
  .panel {
    position: absolute;
    top: 50px;
    height: 650px;
    background: var(--paper);
    overflow: hidden;
    box-shadow: 0 4px 14px rgba(0,0,0,0.18);
  }
  .panel svg { position: absolute; inset: 0; width: 100%; height: 100%; }
  .front-cover { left: 30px; width: 380px; }
  .inside-spread { left: 450px; width: 720px; display: flex; }
  .inside-left, .inside-right { position: relative; width: 360px; height: 650px; }
  .inside-left { border-right: 1px solid #dcdcdc; }

  .brand-name {
    position: absolute;
    font-weight: 500;
    color: var(--ink);
    letter-spacing: 2px;
    text-transform: uppercase;
    line-height: 1.25;
    text-align: center;
  }
  .front-cover .brand-name { left: 25px; top: 252px; width: 200px; font-size: 20px; }
  .inside-right .brand-name { left: 80px; top: 33px; width: 200px; font-size: 20px; }

  .cover-slogan {
    position: absolute;
    left: 30px; top: 318px;
    width: 190px;
    font-size: 11.5px;
    line-height: 1.5;
    color: var(--ink);
    text-align: center;
  }
  .contact-block {
    position: absolute;
    color: #ffffff;
    font-weight: 300;
    text-align: center;
  }
  .contact-block p { padding: 4px 0; }
  .contact-block .phone { font-size: 12px; letter-spacing: 1px; }
  .contact-block .web { font-size: 11.5px; border-top: 1px solid rgba(255,255,255,0.5); border-bottom: 1px solid rgba(255,255,255,0.5); }
  .contact-block .warranty { font-size: 11.5px; }
  .contact-block strong { font-weight: 500; }
  .front-cover .contact-block { left: 170px; top: 528px; width: 195px; }
  .inside-left .contact-block { left: 70px; top: 383px; width: 220px; }

  .spread-slogan {
    position: absolute;
    top: 522px;
    font-size: 15px;
    font-weight: 300;
    letter-spacing: 1px;
    color: #ffffff;
    white-space: nowrap;
  }
  .inside-left .spread-slogan { left: 22px; }
  .inside-right .spread-slogan { left: 4px; }
</style>
</head>
<body>

<section class="panel front-cover">
  <svg viewBox="0 0 380 650" preserveAspectRatio="none">
    <defs>
      <linearGradient id="drivewayTones" x1="0" y1="0" x2="0" y2="1">
        <stop offset="0" stop-color="#7f9a6a"/>
        <stop offset="0.5" stop-color="#b9b6ad"/>
        <stop offset="1" stop-color="#cfcbc2"/>
      </linearGradient>
      <linearGradient id="frontyardTones" x1="0" y1="0" x2="1" y2="1">
        <stop offset="0" stop-color="#6f7b5c"/>
        <stop offset="1" stop-color="#a9a69c"/>
      </linearGradient>
    </defs>
    <polygon class="corner-accent" points="0,0 140,0 140,172 0,100" fill="var(--coral)"/>
    <polygon class="field-light" points="0,114 300,292 118,540 0,472" fill="var(--mist)"/>
    <polygon class="project-photo" role="img" aria-label="Photo of a curved concrete driveway leading to a house" points="150,0 380,0 380,168 150,168" fill="url(#drivewayTones)"/>
    <polygon class="project-photo" role="img" aria-label="Photo of an interlocking stone front walkway with planted beds" points="180,178 380,178 380,320 335,300" fill="url(#frontyardTones)"/>
    <polygon class="field-dark" points="290,290 380,340 380,650 310,650 128,553" fill="var(--charcoal)"/>
    <polygon class="corner-accent" points="0,492 262,650 0,650" fill="var(--coral)"/>
  </svg>
  <div class="brand-name">Fernhollow<br>Landscaping</div>
  <p class="cover-slogan">The experience you want.<br>The service you expect.<br>And the value you deserve.</p>
  <div class="contact-block">
    <p class="phone">416 • 555 • 0187</p>
    <p class="web">www.fernhollowlandscaping.example</p>
    <p class="warranty">Guranteed 24 month warranty</p>
  </div>
</section>

<section class="panel inside-spread">
  <div class="inside-left">
    <svg viewBox="0 0 360 650" preserveAspectRatio="none">
      <defs>
        <linearGradient id="poolTones" x1="0" y1="0" x2="1" y2="1">
          <stop offset="0" stop-color="#6d7a5a"/>
          <stop offset="0.45" stop-color="#2f63b8"/>
          <stop offset="1" stop-color="#7d7a74"/>
        </linearGradient>
      </defs>
      <polygon class="corner-accent" points="252,0 360,0 360,112" fill="var(--coral)"/>
      <polygon class="field-light" points="360,125 360,340 205,340" fill="var(--mist)"/>
      <polygon class="field-mint" points="0,225 160,340 0,340" fill="var(--mint)"/>
      <polygon class="project-photo" role="img" aria-label="Photo of a backyard pool with a stone waterfall and patio" points="0,0 240,0 345,118 190,335 0,205" fill="url(#poolTones)"/>
      <rect class="band-dark" x="0" y="348" width="360" height="150" fill="var(--charcoal)"/>
      <rect class="band-coral" x="0" y="506" width="360" height="144" fill="var(--coral)"/>
    </svg>
    <div class="contact-block">
      <p class="phone">416 • 555 • 0187</p>
      <p class="web">www.fernhollowlandscaping.example</p>
      <p class="warranty">Guranteed <strong>24 month warranty</strong></p>
    </div>
    <p class="spread-slogan">THE EXPERIENCE YOU WANT. THE SERVICE</p>
  </div>

  <div class="inside-right">
    <svg viewBox="0 0 360 650" preserveAspectRatio="none">
      <defs>
        <linearGradient id="siteTones" x1="0" y1="0" x2="0" y2="1">
          <stop offset="0" stop-color="#c9ccd0"/>
          <stop offset="0.45" stop-color="#9a9a98"/>
          <stop offset="1" stop-color="#b3aea6"/>
        </linearGradient>
      </defs>
      <rect class="band-light" x="0" y="0" width="360" height="108" fill="var(--silver)"/>
      <polygon class="field-mint" points="0,116 170,116 0,335" fill="var(--mint)"/>
      <polygon class="field-light" points="20,335 185,122 345,280 90,280" fill="var(--mist)"/>
      <polygon class="corner-accent" points="198,116 360,116 360,250" fill="var(--coral)"/>
      <polygon class="field-slate" points="0,345 150,500 0,500" fill="var(--slate)"/>
      <polygon class="project-photo" role="img" aria-label="Photo of a crew pouring a commercial concrete lot" points="92,286 352,286 352,500 150,500 60,395" fill="url(#siteTones)"/>
      <rect class="band-coral" x="0" y="506" width="360" height="144" fill="var(--coral-dark)"/>
      <line x1="90" y1="590" x2="120" y2="565" stroke="#ffffff" stroke-width="1"/>
      <line x1="210" y1="630" x2="240" y2="605" stroke="#ffffff" stroke-width="1"/>
    </svg>
    <div class="brand-name">Fernhollow<br>Landscaping</div>
    <p class="spread-slogan">YOU EXPECT. AND THE VALUE YOU DESERVE.</p>
  </div>
</section>

</body>
</html>
```